Disposable Mini Sauce Pot Design for Asian Chain Food Brands

We operate a Hainan Chicken Rice takeout brand under the name Spin4Rye, with our official website: www.Spin4Rye.com.
We offer four signature house sauces and are launching brand-new packaging for our sauce line. We require custom graphic designs exclusively for the sauce cup lids.
Product Material & Base Specs
The sauce cups are made of PP plastic, available in two translucent base options: Translucent White and Translucent Orange.
Four Sauce Varieties for Individual Lid Designs
1. Red Sauce – Fried Sweet Chili Sauce
2.Green Sauce – Scallion Oil Dressing
3.Sweet Soy Sauce
4.Sweet Red Sauce (Special for Fried Chicken)
Differentiate each sauce lid design through unique graphics, typography, or illustrative elements for easy customer identification.
The marking NET WT 2 OZ must be clearly printed on every lid.
**There is no need to print full descriptive text or the full name of the sauces on each lid; the design only needs to clearly differentiate the four sauce varieties.
**Please reference the original design style and brand color palette shown on our official website, and feel free to fully unleash your creativity.

```html
<!DOCTYPE html>
<html lang="en">
<head>
<meta charset="utf-8">
<title>Spin4Rye Sauce Lids</title>
<link rel="stylesheet" href="https://fonts.googleapis.com/css2?family=Anton&family=Archivo+Black&family=Londrina+Solid:wght@900&family=Roboto:wght@400&family=Titan+One&display=swap">
<style>
  :root {
    --cream: #f6f2ee;
    --pink: #f72064;
    --pink-soft: #fd5a92;
    --pink-deep: #8a0a30;
    --yellow: #ffe600;
    --lime: #d4e82e;
    --lime-soft: #c6d320;
    --olive: #7d8c10;
    --ink: #1f1f1d;
    --orange: #fc6d08;
    --orange-soft: #fd8a3a;
    --brown: #6b2a05;
    --red: #e8000f;
    --violet: #c77cf0;
    --violet-soft: #d597ff;
    --plum: #5a1f66;
    --gold: #fdd000;
  }
  * { margin: 0; padding: 0; box-sizing: border-box; }
  html, body { width: 1200px; height: 1200px; overflow: hidden; background: #fff; }
  .sheet { position: relative; width: 1200px; height: 1200px; }

  .lid {
    position: absolute; width: 451px; height: 510px;
    border-radius: 66px; overflow: hidden;
    box-shadow: 4px 5px 4px rgba(0,0,0,.55);
  }
  .lid--chili { left: 138px; top: 80px; background: var(--pink); }
  .lid--scallion { left: 612px; top: 80px; background: var(--lime); }
  .lid--red { left: 138px; top: 611px; background: var(--orange); }
  .lid--soy { left: 612px; top: 611px; background: var(--violet); }

  .mascot-area {
    position: absolute; left: 40px; top: 60px; width: 420px; height: 480px;
    border-radius: 45% 55% 40% 60%;
  }
  .lid--chili .mascot-area { background: radial-gradient(ellipse at 50% 45%, var(--pink-soft) 55%, transparent 72%); }
  .lid--scallion .mascot-area { background: radial-gradient(ellipse at 50% 45%, var(--lime-soft) 55%, transparent 72%); }
  .lid--red .mascot-area { background: radial-gradient(ellipse at 50% 45%, var(--orange-soft) 55%, transparent 72%); }
  .lid--soy .mascot-area { background: radial-gradient(ellipse at 50% 45%, var(--violet-soft) 55%, transparent 72%); }

  .brand {
    position: absolute; left: 0; right: 0; top: 44px; text-align: center;
    font-family: "Archivo Black", sans-serif; font-size: 30px; color: var(--cream);
    letter-spacing: -0.5px;
  }
  .lid--scallion .brand { color: var(--ink); }

  .net-wt {
    position: absolute; left: 0; right: 0; top: 470px; text-align: center;
    font-family: "Roboto", sans-serif; font-size: 16px; color: var(--cream);
  }
  .lid--scallion .net-wt { color: var(--ink); }

  .word {
    position: absolute; left: 0; right: 0; text-align: center;
    line-height: 1; white-space: nowrap; transform: rotate(-3deg);
  }

  /* Fried sweet chili */
  .lid--chili .word { font-family: "Archivo Black", sans-serif; letter-spacing: -2px; }
  .chili-fried { top: 110px; font-size: 104px; color: var(--cream); left: -6px;
    text-shadow: 1px 1px 0 var(--pink-deep), 2px 2px 0 var(--pink-deep), 3px 3px 0 var(--pink-deep), 4px 4px 0 var(--pink-deep), 5px 5px 0 var(--pink-deep), 6px 6px 0 var(--pink-deep); }
  .chili-sweet { top: 200px; font-size: 112px; color: var(--yellow); left: 14px;
    text-shadow: 1px 1px 0 var(--pink-deep), 2px 2px 0 var(--pink-deep), 3px 3px 0 var(--pink-deep), 4px 4px 0 var(--pink-deep), 5px 5px 0 var(--pink-deep), 6px 6px 0 var(--pink-deep); }
  .chili-chili { top: 300px; font-size: 112px; color: var(--cream); left: 8px;
    text-shadow: 1px 1px 0 var(--pink-deep), 2px 2px 0 var(--pink-deep), 3px 3px 0 var(--pink-deep), 4px 4px 0 var(--pink-deep), 5px 5px 0 var(--pink-deep), 6px 6px 0 var(--pink-deep); }

  .tag {
    position: absolute; transform: rotate(-3deg); text-align: center;
    font-family: "Archivo Black", sans-serif; line-height: 1;
  }
  .tag--chili { left: 176px; top: 405px; width: 132px; height: 44px; font-size: 36px;
    background: var(--yellow); color: var(--pink); box-shadow: 4px 4px 0 var(--pink-deep); padding-top: 4px; }

  /* Scallion oil */
  .scallion-name { top: 94px; font-family: "Londrina Solid", sans-serif; font-size: 112px; color: var(--ink); left: -12px;
    text-shadow: 4px 4px 0 var(--olive), 5px 5px 0 var(--olive), 6px 6px 0 var(--olive); }
  .scallion-oil { top: 168px; font-family: "Titan One", sans-serif; font-size: 210px; color: var(--ink); left: 12px; letter-spacing: -4px;
    transform: rotate(-2deg); text-shadow: 4px 4px 0 var(--olive), 6px 6px 0 var(--olive), 8px 8px 0 var(--olive); }
  .tag--dressing { left: 118px; top: 400px; width: 206px; height: 52px; font-size: 36px;
    background: var(--cream); color: var(--ink); box-shadow: 4px 4px 0 var(--olive); padding-top: 7px; }

  /* Sweet red */
  .lid--red .word, .lid--soy .word { font-family: "Anton", sans-serif; }
  .red-sweet { top: 104px; font-size: 178px; color: var(--cream); left: 10px; letter-spacing: -3px;
    text-shadow: 2px 2px 0 var(--brown), 4px 4px 0 var(--brown), 6px 6px 0 var(--brown), 8px 8px 0 var(--brown); }
  .red-red { top: 280px; font-family: "Archivo Black", sans-serif !important; font-size: 136px; color: var(--cream); left: 10px; letter-spacing: -4px; line-height: 0.95;
    text-shadow: 2px 2px 0 var(--brown), 4px 4px 0 var(--brown), 6px 6px 0 var(--brown), 8px 8px 0 var(--brown); }
  .tag--red { left: 135px; top: 398px; width: 170px; height: 58px; font-size: 42px;
    background: var(--red); color: var(--cream); box-shadow: 5px 5px 0 var(--brown); padding-top: 8px; }

  /* Sweet soy */
  .soy-sweet { top: 98px; font-size: 150px; color: var(--gold); left: 22px;
    text-shadow: 2px 2px 0 var(--plum), 4px 4px 0 var(--plum), 6px 6px 0 var(--plum), 8px 8px 0 var(--plum); }
  .soy-soy { top: 222px; font-size: 178px; color: var(--cream); left: 8px; letter-spacing: 4px;
    text-shadow: 2px 2px 0 var(--plum), 4px 4px 0 var(--plum), 6px 6px 0 var(--plum), 8px 8px 0 var(--plum); }
  .tag--soy { left: 143px; top: 392px; width: 168px; height: 64px; font-size: 42px;
    background: var(--gold); color: var(--plum); box-shadow: 5px 5px 0 var(--plum); padding-top: 11px; }

  .spark { position: absolute; }
</style>
</head>
<body>
<main class="sheet">

  <section class="lid lid--chili">
    <div class="mascot-area" role="img" aria-label="Faint brand mascot silhouette in the background"></div>
    <p class="brand">Spin4Rye</p>
    <svg class="spark" style="left:38px;top:100px" width="40" height="36" viewBox="0 0 40 36" aria-hidden="true">
      <path d="M4 22 L22 30 M20 2 L28 24 M34 12 L32 26" stroke="#ffe600" stroke-width="5" stroke-linecap="round"/>
    </svg>
    <p class="word chili-fried">FRIED</p>
    <p class="word chili-sweet">SWEET</p>
    <p class="word chili-chili">CHILI</p>
    <p class="tag tag--chili">SAUCE</p>
    <p class="net-wt">NET WT. 2 OZ</p>
  </section>

  <section class="lid lid--scallion">
    <div class="mascot-area" role="img" aria-label="Faint brand mascot silhouette in the background"></div>
    <p class="brand">Spin4Rye</p>
    <p class="word scallion-name">SCALLION</p>
    <p class="word scallion-oil">OIL</p>
    <p class="tag tag--dressing">DRESSING</p>
    <p class="net-wt">NET WT. 2 OZ</p>
  </section>

  <section class="lid lid--red">
    <div class="mascot-area" role="img" aria-label="Faint brand mascot silhouette in the background"></div>
    <p class="brand">Spin4Rye</p>
    <p class="word red-sweet">SWEET</p>
    <p class="word red-red">RED</p>
    <p class="tag tag--red">SAUCE</p>
    <p class="net-wt">NET WT. 2 OZ</p>
  </section>

  <section class="lid lid--soy">
    <div class="mascot-area" role="img" aria-label="Faint brand mascot silhouette in the background"></div>
    <p class="brand">Spin4Rye</p>
    <svg class="spark" style="left:38px;top:104px" width="40" height="36" viewBox="0 0 40 36" aria-hidden="true">
      <circle cx="8" cy="8" r="7" fill="#f6f2ee"/><circle cx="24" cy="6" r="3" fill="#f6f2ee"/><circle cx="14" cy="26" r="4" fill="#f6f2ee"/>
    </svg>
    <p class="word soy-sweet">SWEET</p>
    <p class="word soy-soy">SOY</p>
    <p class="tag tag--soy">SAUCE</p>
    <p class="net-wt">NET WT. 2 OZ</p>
  </section>

</main>
</body>
</html>
```